Brochure for new townhouse development

We need a brochure created for our new townhouse development that we can provide to potential purchasers for off-the-plan sales.

2 similar examples are attached.

Brochure content is to include the text as per the attached word document (brochure text) and as follows:
Cover
The Development
At a Glance
The Location - also to include the 2d map and aerial photo (have included screenshot of map and aerial photo as a placeholder, to be replaced in the final version)
Plans - include 3d floor plans, I have included a sample 3d floor plan as a placeholder, this is to be replaced in the final version.
Finishes - as per word document attached, and colour samples attached
Specifications - as per word document attached
Subdivision plan - I have attached a plan which can be used as a placeholder, the final version will be ready next week and is to be replaced in the final version
Landscape plan - as per attached
Rental assessment - as per attached
Stake your Claim

Renders of the building are attached and can be used throughout the brochure.

There is no company name or logo to include.

We have other upcoming developments and would look to reuse the winning brochure so there is future and ongoing work.

```html
<!DOCTYPE html>
<html lang="en">
<head>
<meta charset="utf-8">
<title>Perfectly Positioned Urban Living – Townhouse Brochure</title>
<link rel="stylesheet" href="https://fonts.googleapis.com/css2?family=Open+Sans:wght@400;600;700&display=swap">
<style>
  :root {
    --stage: #e6e6e6;
    --paper: #ffffff;
    --paper-soft: #f3f3f3;
    --charcoal: #4a4a4a;
    --charcoal-dark: #3c3c3c;
    --accent-grey: #b5b5b5;
    --accent-light: #d2d2d2;
    --ink: #333333;
    --ink-light: #f0f0f0;
    --sky-top: #b9d3ea;
    --sky-low: #e6d6e2;
    --timber: #b99a78;
    --ground: #6f7376;
  }
  * { box-sizing: border-box; margin: 0; padding: 0; }
  html, body { width: 1200px; height: 900px; overflow: hidden; }
  body {
    background: var(--stage);
    font-family: "Open Sans", Arial, sans-serif;
    color: var(--ink);
    position: relative;
  }

  .page {
    position: absolute;
    background: var(--paper);
    box-shadow: 0 2px 10px rgba(0,0,0,0.12);
    overflow: hidden;
  }
  .accent-band {
    position: absolute;
    top: 0; left: 0;
    height: 26px;
  }
  .accent-band--dark { background: var(--accent-grey); }
  .accent-band--light { background: var(--accent-light); }

  .render {
    position: absolute;
    background: linear-gradient(180deg, var(--sky-top) 0%, var(--sky-low) 45%, var(--timber) 46%, #d9d4cd 78%, var(--ground) 100%);
  }
  .render--garage {
    background: linear-gradient(180deg, var(--sky-top) 0%, #dcd7e6 30%, #e9e9ea 31%, var(--timber) 60%, #3e4042 61%, var(--ground) 100%);
  }

  .title-block {
    position: absolute;
    background: var(--charcoal);
    color: var(--ink-light);
    text-align: center;
    padding: 8px 16px 7px;
  }
  .title-block__heading { font-weight: 700; font-size: 14px; letter-spacing: 0.2px; }
  .title-block__address { font-weight: 600; font-size: 9px; margin-top: 1px; }

  /* Cover */
  .cover { left: 320px; top: 30px; width: 560px; height: 390px; background: var(--paper-soft); }
  .cover .accent-band--dark { width: 250px; }
  .cover .accent-band--light { left: 250px; width: 310px; }
  .cover .render { left: 40px; top: 50px; width: 490px; height: 270px; }
  .cover .title-block { right: 30px; top: 296px; }

  /* Spread */
  .spread-left { left: 40px; top: 450px; width: 560px; height: 420px; }
  .spread-right { left: 600px; top: 450px; width: 560px; height: 420px; box-shadow: 0 2px 10px rgba(0,0,0,0.12); }
  .spread-left .accent-band--dark { width: 180px; }
  .spread-right .accent-band--dark { width: 200px; }
  .spread-right .accent-band--light { left: 200px; width: 60px; }
  .spread-left::after {
    content: ""; position: absolute; right: 0; top: 0; bottom: 0; width: 14px;
    background: linear-gradient(90deg, rgba(0,0,0,0) 0%, rgba(0,0,0,0.06) 100%);
  }

  .development {
    position: absolute; left: 34px; top: 48px; width: 270px; height: 290px;
    background: var(--charcoal);
    color: var(--ink-light);
    padding: 18px 18px;
  }
  .development__heading {
    font-size: 13px; font-weight: 700; padding-bottom: 4px; margin-bottom: 10px;
    border-bottom: 1px solid var(--ink-light); display: inline-block;
  }
  .development p { font-size: 8.6px; line-height: 1.42; margin-bottom: 6px; }

  .glance { position: absolute; left: 326px; top: 70px; width: 210px; }
  .glance__heading {
    font-size: 12px; font-weight: 700; padding-bottom: 3px; margin-bottom: 8px;
    border-bottom: 1px solid var(--ink); display: inline-block;
  }
  .glance__intro { font-size: 8.6px; line-height: 1.4; margin-bottom: 4px; }
  .glance__list { list-style: none; }
  .glance__list li {
    font-size: 8.6px; line-height: 1.4; padding-left: 10px; position: relative; margin-bottom: 2px;
  }
  .glance__list li::before {
    content: ""; position: absolute; left: 0; top: 5px; width: 3px; height: 3px;
    border-radius: 50%; background: var(--ink);
  }
  .spread-left .title-block { right: 26px; top: 352px; }

  .spread-right .render { left: 46px; top: 40px; width: 470px; height: 290px; }
  .section-label {
    position: absolute; left: 46px; top: 356px;
    font-size: 10px; font-weight: 700; letter-spacing: 0.6px;
    padding-bottom: 3px; border-bottom: 1px solid var(--ink); width: 72px;
  }
  .spread-right .title-block { right: 30px; top: 318px; }
</style>
</head>
<body>

  <section class="page cover">
    <div class="accent-band accent-band--dark"></div>
    <div class="accent-band accent-band--light"></div>
    <div class="render" role="img" aria-label="Architectural render of two gabled timber-clad townhouses behind low white garden walls at dusk"></div>
    <div class="title-block">
      <div class="title-block__heading">Perfectly Positioned Urban Living</div>
      <div class="title-block__address">48 Larchfield Road</div>
    </div>
  </section>

  <section class="page spread-left">
    <div class="accent-band accent-band--dark"></div>
    <article class="development">
      <h2 class="development__heading">The Development</h2>
      <p>48 Larchfield Road, Elmwood is a boutique development of six townhouses ideally placed for easy access to shops, cafes, schools and parks.</p>
      <p>Two blocks of three homes offer stylish, low-maintenance living with a warm timber and render palette chosen to suit the leafy street.</p>
      <p>On the ground floor, open-plan living and dining flow to a sheltered courtyard, with a modern kitchen at the heart of the home.</p>
      <p>Upstairs are two double bedrooms, each served by a tiled bathroom, with the master suite enjoying a generous walk-in wardrobe.</p>
      <p>Architecturally designed with quality finishes throughout, these homes are due for completion next year, so now is the time to make your move.</p>
    </article>
    <article class="glance">
      <h2 class="glance__heading">At a Glance</h2>
      <p class="glance__intro">Two blocks of three architecturally designed townhouses. Each townhouse includes:</p>
      <ul class="glance__list">
        <li>Open-plan living, dining and high-spec kitchen</li>
        <li>Seamless flow to easy care courtyard garden</li>
        <li>Two double bedrooms, each with built-in wardrobes (walk-in to master)</li>
        <li>Two tiled bathrooms</li>
        <li>Single internal-access garage with laundry</li>
        <li>Smart design, high-quality fixtures and fittings, and freehold titles</li>
      </ul>
    </article>
    <div class="title-block">
      <div class="title-block__heading">Perfectly Positioned Urban Living</div>
      <div class="title-block__address">48 Larchfield Road</div>
    </div>
  </section>

  <section class="page spread-right">
    <div class="accent-band accent-band--dark"></div>
    <div class="accent-band accent-band--light"></div>
    <div class="render render--garage" role="img" aria-label="Exterior render of townhouses with white rendered garages, dark garage doors and timber-clad upper floors along a shared driveway"></div>
    <div class="section-label">EXTERIOR</div>
    <div class="title-block">
      <div class="title-block__heading">Perfectly Positioned Urban Living</div>
      <div class="title-block__address">48 Larchfield Road</div>
    </div>
  </section>

</body>
</html>
```